Business Card Revision

Need to redesign my business cards for a new professional look. We are a courier company. You can go to www.qvrunners.com to see what we do. The trucks have an old company name (Sprout) on them but that is the company we are just now
changing the name.

Target Market(s)

Potential clients. We service the automotive, plumbing, printing, air freight industries as well as many others.

Industry/Entity Type

Business

Contact Information for Business Card

QVmotion
20864 Lark Fenmore Parkway
Cincinnati, Oh 45873

Thomas R. Wendall
President

tom@qvrunners.com

Main: (513) 555-0147

```html
<!DOCTYPE html>
<html lang="en">
<head>
<meta charset="utf-8">
<title>QV Runners – Business Card</title>
<link href="https://fonts.googleapis.com/css2?family=Tinos:wght@400;700&display=swap" rel="stylesheet">
<style>
  :root {
    --page-bg: #e9e7e3;
    --card-green: #3aa84a;
    --card-green-dark: #23803a;
    --panel-white: #ffffff;
    --panel-shade: #d9dde3;
    --edge-navy: #1d3a6b;
    --brand-blue: #1f78c1;
    --ink-navy: #263248;
  }
  * { margin: 0; padding: 0; box-sizing: border-box; }
  html, body {
    width: 1200px; height: 900px; overflow: hidden;
    background: var(--page-bg);
  }
  .canvas {
    position: relative; width: 1200px; height: 900px;
    display: flex; align-items: center; justify-content: center;
  }
  .business-card {
    position: relative; width: 900px; height: 514px;
    box-shadow: 0 10px 30px rgba(0,0,0,0.18);
    overflow: hidden;
  }
  .card-background { position: absolute; inset: 0; }
  .card-content {
    position: absolute; inset: 0;
    display: flex; flex-direction: column; align-items: center;
    font-family: "Tinos", "Times New Roman", serif;
    color: var(--ink-navy);
    text-align: center;
  }
  .brand-name {
    margin-top: 92px;
    font-size: 84px; font-weight: 700; line-height: 1;
    color: var(--brand-blue);
    letter-spacing: 1px;
  }
  .person-name {
    margin-top: 48px;
    font-size: 40px; font-weight: 700; line-height: 1;
  }
  .person-title {
    margin-top: 4px;
    font-size: 26px; font-weight: 700; line-height: 1;
    color: var(--brand-blue);
  }
  .contact-lines { margin-top: 26px; font-size: 28px; line-height: 1.15; }
  .address-lines { margin-top: 20px; font-size: 30px; font-weight: 700; line-height: 1.1; }
</style>
</head>
<body>
<main class="canvas">
  <section class="business-card">
    <svg class="card-background" viewBox="0 0 900 514" width="900" height="514" aria-hidden="true">
      <defs>
        <linearGradient id="greenPanel" x1="0" y1="0" x2="0" y2="1">
          <stop offset="0" stop-color="var(--card-green)"/>
          <stop offset="1" stop-color="var(--card-green-dark)"/>
        </linearGradient>
        <radialGradient id="whitePanel" cx="0.5" cy="0.45" r="0.6">
          <stop offset="0.7" stop-color="var(--panel-white)"/>
          <stop offset="1" stop-color="var(--panel-shade)"/>
        </radialGradient>
      </defs>
      <rect class="green-field" width="900" height="514" fill="url(#greenPanel)"/>
      <path class="panel-edge" d="M200 0 L700 0 C812 120 822 390 718 514 L182 514 C78 390 88 120 200 0 Z" fill="var(--edge-navy)"/>
      <path class="white-panel" d="M214 0 L686 0 C792 120 800 390 702 514 L198 514 C100 390 108 120 214 0 Z" fill="url(#whitePanel)"/>
    </svg>
    <div class="card-content">
      <div class="brand-name">QV Runners</div>
      <div class="person-name">Thomas R. Wendall</div>
      <div class="person-title">President</div>
      <div class="contact-lines">
        <div class="phone">(513) 555-0147</div>
        <div class="email">tom@qvrunners.com</div>
      </div>
      <div class="address-lines">
        <div>20864 Lark Fenmore Parkway</div>
        <div>Cincinnati, Oh 45873</div>
      </div>
    </div>
  </section>
</main>
</body>
</html>
```